VerdaTurfix - 11" x 4" Door Hanger, full color both sides

We need a door hanger designed, 11" x 4", full color both sides, We are a lawn care company that provides lawn mowing, and other services to clients. This door hanger will be place on the 9 neighbors of our current clients. The ad needs to state that we provided lawn service to one of their neighbors today, and that we are in their neighborhood each week on that day. The door hanger will have 4 printings, substituting the day of Tuesday, Wednesday, Thursday, and Friday. All the art work and text will remain the same except the day of the week. For information about VerdaTurfix, please visit our website www.verdaturfix.net. The main emphasis of the message should be that we are their every week on that day, and the benefits to them of using our service (ie. quality time with their family, golf, sports, resting, etc., instead of mowing the lawn). At the bottom of the door hanger will be a coupon offering their tenth (10th) lawn service free, which is the same as a 10% discount.

I have uploaded a template files for the front and back of an 11 x 4 door hanger, The templates are pdf, jpeg, or eps files. The final product can be a pdf, jpeg, or eps file.

Target Market(s)

Neighbors of our existing clients

Industry/Entity Type

Lawn Care

Font styles to use
Serif

Requirements
Must have
• Professional design and art, Short conversational message that relays the following thoughts:
• 1. We mowed your neighbor's lawn today!
• 2. We are in your neighborhood every Tuesday!
• 3. Our lawn service is guaranteed.
• 4. Call to action - Call us today! 555-014-7382
• 5. Of course our contact info, name, phone number, website address.
• 6. Coupon at bottom for "10th lawn service Free!"
Nice to have
• Art work from our website is fine to use, That carries our theme throughout our campaign.
Should not have
• Very wordy. This is basically a billboard, Have very few seconds to grab their attention.

```html
<!DOCTYPE html>
<html lang="en">
<head>
<meta charset="utf-8">
<title>VerdaTurfix Door Hanger – Front and Back</title>
<link href="https://fonts.googleapis.com/css2?family=Montserrat:wght@400;500&family=Nunito:wght@600;700;800;900&display=swap" rel="stylesheet">
<style>
  :root {
    --page: #ffffff;
    --panel: #f3f3f3;
    --ink: #000000;
    --white: #ffffff;
    --red: #e8383d;
    --grass-dark: #1d4a12;
    --grass: #3a8a1f;
    --grass-light: #6fb33a;
    --coupon-box: #2a2a2a;
  }
  html, body {
    margin: 0;
    width: 1200px;
    height: 1200px;
    overflow: hidden;
    background: var(--page);
  }
  .canvas { position: relative; width: 1200px; height: 1200px; }
  .panel { position: absolute; top: 0; height: 1200px; background: var(--panel); }
  .panel--front { left: 140px; width: 454px; }
  .panel--back { left: 618px; width: 458px; }
  .hanger { position: absolute; top: 10px; width: 429px; height: 1180px; }
  .hanger--front { left: 152px; }
  .hanger--back { left: 635px; width: 427px; }
  .brand { font-family: "Montserrat", sans-serif; font-weight: 500; fill: var(--white); }
  .side-tag { font-family: "Nunito", sans-serif; font-weight: 800; fill: var(--red); font-size: 24px; }
  .headline { font-family: "Nunito", sans-serif; font-weight: 900; fill: var(--white); }
  .body-copy { font-family: "Nunito", sans-serif; font-weight: 800; fill: var(--white); }
  .accent { font-family: "Nunito", sans-serif; font-weight: 900; fill: var(--red); }
  .small-copy { font-family: "Nunito", sans-serif; font-weight: 600; fill: var(--white); }
  .coupon-num { font-family: "Montserrat", sans-serif; font-weight: 400; fill: var(--white); }
  .service-item { font-family: "Montserrat", sans-serif; font-weight: 500; fill: var(--white); font-size: 16px; letter-spacing: -0.5px; }
</style>
</head>
<body>
<div class="canvas">
  <div class="panel panel--front"></div>
  <div class="panel panel--back"></div>

  <!-- Front side -->
  <svg class="hanger hanger--front" viewBox="0 0 429 1180" xmlns="http://www.w3.org/2000/svg">
    <defs>
      <clipPath id="front-shape"><rect width="429" height="1180" rx="28"/></clipPath>
      <linearGradient id="front-grass" x1="0" y1="0" x2="0" y2="1">
        <stop offset="0" stop-color="var(--grass)"/>
        <stop offset="0.5" stop-color="#2f7a18"/>
        <stop offset="1" stop-color="var(--grass-dark)"/>
      </linearGradient>
      <linearGradient id="coupon-grass" x1="0" y1="0" x2="1" y2="1">
        <stop offset="0" stop-color="#5aa12c"/>
        <stop offset="1" stop-color="var(--grass-light)"/>
      </linearGradient>
      <linearGradient id="mower" x1="0" y1="0" x2="1" y2="0">
        <stop offset="0" stop-color="#3b3f3a"/>
        <stop offset="0.55" stop-color="#4a4d48"/>
        <stop offset="0.7" stop-color="#d4262a"/>
        <stop offset="1" stop-color="#b51c20"/>
      </linearGradient>
    </defs>
    <g clip-path="url(#front-shape)">
      <rect class="top-band" width="429" height="386" fill="var(--ink)"/>
      <line x1="286" y1="179" x2="429" y2="179" stroke="var(--white)" stroke-width="3"/>
      <circle cx="214" cy="179" r="72" fill="var(--white)"/>
      <text class="side-tag" x="214" y="188" text-anchor="middle">FRONT</text>
      <text class="brand" x="214" y="366" text-anchor="middle" font-size="42">VERDATURFIX</text>

      <rect role="img" aria-label="Close-up photo of a freshly mowed green lawn" y="386" width="429" height="570" fill="url(#front-grass)"/>

      <text class="headline" x="214" y="498" text-anchor="middle" font-size="74">We</text>
      <text class="headline" x="214" y="553" text-anchor="middle" font-size="74">mowed</text>
      <text class="headline" x="214" y="596" text-anchor="middle" font-size="44">your neighbor’s</text>
      <text class="headline" x="214" y="636" text-anchor="middle" font-size="44">lawn</text>
      <text class="headline" x="214" y="725" text-anchor="middle" font-size="96" letter-spacing="-3">TODAY!</text>

      <text class="body-copy" x="214" y="788" text-anchor="middle" font-size="22">Every Tuesday we will be here</text>
      <text class="body-copy" x="214" y="856" text-anchor="middle" font-size="36" letter-spacing="-1">Call us now!</text>
      <text class="body-copy" x="214" y="893" text-anchor="middle" font-size="36" letter-spacing="-1">555-014-7382</text>

      <rect role="img" aria-label="Sunlit lawn grass behind the coupon" y="956" width="429" height="224" fill="url(#coupon-grass)"/>
      <rect role="img" aria-label="Red lawn mower seen from above" x="320" y="958" width="109" height="222" fill="url(#mower)"/>
      <line x1="0" y1="956" x2="429" y2="956" stroke="var(--white)" stroke-width="2" stroke-dasharray="3 3"/>
      <g class="scissors" fill="none" stroke="var(--white)" stroke-width="3">
        <circle cx="40" cy="948" r="5"/>
        <circle cx="40" cy="966" r="5"/>
        <line x1="44" y1="951" x2="82" y2="962"/>
        <line x1="44" y1="963" x2="82" y2="950"/>
      </g>

      <rect class="coupon-box" x="37" y="966" width="137" height="214" fill="var(--coupon-box)"/>
      <text class="coupon-num" x="42" y="1070" font-size="104" letter-spacing="-8">10</text>
      <text class="coupon-num" x="128" y="1014" font-size="34">TH</text>
      <text class="body-copy" x="105" y="1098" text-anchor="middle" font-size="17" letter-spacing="-0.5">LAWN SERVICE</text>
      <text class="coupon-num" x="105" y="1150" text-anchor="middle" font-size="56" letter-spacing="-2">FREE</text>
      <text class="brand" x="190" y="1066" font-size="24">VERDATURFIX</text>
    </g>
  </svg>

  <!-- Back side -->
  <svg class="hanger hanger--back" viewBox="0 0 427 1180" xmlns="http://www.w3.org/2000/svg">
    <defs>
      <clipPath id="back-shape"><rect width="427" height="1180" rx="28"/></clipPath>
      <linearGradient id="family-photo" x1="0" y1="0" x2="1" y2="1">
        <stop offset="0" stop-color="#c9c58a"/>
        <stop offset="0.45" stop-color="#8fa35a"/>
        <stop offset="1" stop-color="#4f8a2a"/>
      </linearGradient>
      <linearGradient id="back-grass" x1="0" y1="0" x2="0" y2="1">
        <stop offset="0" stop-color="#050805"/>
        <stop offset="0.35" stop-color="#163a0e"/>
        <stop offset="1" stop-color="#245a14"/>
      </linearGradient>
    </defs>
    <g clip-path="url(#back-shape)">
      <rect width="427" height="1180" fill="url(#back-grass)"/>
      <rect class="top-band" width="427" height="386" fill="var(--ink)"/>
      <line x1="0" y1="179" x2="142" y2="179" stroke="var(--white)" stroke-width="3"/>
      <circle cx="214" cy="179" r="72" fill="var(--white)"/>
      <text class="side-tag" x="214" y="188" text-anchor="middle">BACK</text>
      <text class="brand" x="214" y="366" text-anchor="middle" font-size="42">VERDATURFIX</text>

      <path role="img" aria-label="Photo of a happy family playing together on a sunny lawn" d="M0 386 H427 V668 Q210 790 0 690 Z" fill="url(#family-photo)"/>
      <path d="M0 690 Q210 790 427 668" fill="none" stroke="var(--white)" stroke-width="8"/>

      <text class="accent" x="214" y="802" text-anchor="middle" font-size="22">Let’s get your lawn</text>
      <text class="accent" x="214" y="824" text-anchor="middle" font-size="22">care started!</text>
      <text class="small-copy" x="214" y="846" text-anchor="middle" font-size="14">We will take care of your lawn care needs,</text>
      <text class="small-copy" x="214" y="865" text-anchor="middle" font-size="14">which allows you to spend quality time with your family!</text>
      <text class="headline" x="214" y="908" text-anchor="middle" font-size="31" letter-spacing="-0.5">www.verdaturfix.net</text>

      <line x1="60" y1="952" x2="427" y2="952" stroke="var(--white)" stroke-width="2" stroke-dasharray="3 3"/>
      <g class="scissors" fill="none" stroke="var(--white)" stroke-width="3">
        <circle cx="40" cy="942" r="5"/>
        <circle cx="40" cy="960" r="5"/>
        <line x1="44" y1="945" x2="82" y2="956"/>
        <line x1="44" y1="957" x2="82" y2="944"/>
      </g>

      <text class="accent" x="214" y="988" text-anchor="middle" font-size="22" letter-spacing="-0.5">OUR SERVICES</text>
      <text class="service-item" x="214" y="1015" text-anchor="middle">• LAWN CARE</text>
      <text class="service-item" x="214" y="1040" text-anchor="middle">• FERTILIZATION WEED CONTROL</text>
      <text class="service-item" x="214" y="1065" text-anchor="middle">• SPRINKLER REPAIR</text>
      <text class="service-item" x="214" y="1091" text-anchor="middle">• OTHER LAWN CARE SERVICES</text>
      <text class="brand" x="214" y="1128" text-anchor="middle" font-size="30">VERDATURFIX</text>
    </g>
  </svg>
</div>
</body>
</html>
```